Restoration Business Cards

I’m in the water damage restoration industry and we specialize in water, mold, fire and restoration. I’m looking to get new business cards.

Business cards must have my logo with the letters

Z-9 Max
Emergency Restoration

Owner
Derek Vannorman
(555)412-7083
z9maxbuild@mailbox.test
https://www.z9maxbuild.test
Lic #4702859 D-47 K
•Water •Mold •Fire •Restoration
RVFTA Certified #81254039

Add an QR code

```html
<!DOCTYPE html>
<html lang="en">
<head>
<meta charset="utf-8">
<title>Z-9 Max Emergency Restoration – Business Cards</title>
<link rel="stylesheet" href="https://fonts.googleapis.com/css2?family=Montserrat:wght@400;800&display=swap">
<style>
  :root {
    --backdrop: #232323;
    --card-top: #55616c;
    --card-bottom: #3b444d;
    --gold: #d9ad5c;
    --gold-deep: #b07e2e;
    --blue: #5a9ae0;
    --ink-soft: #cfa457;
  }
  * { box-sizing: border-box; margin: 0; padding: 0; }
  html, body { width: 1200px; height: 780px; overflow: hidden; }
  body {
    background: var(--backdrop);
    font-family: "Montserrat", Arial, sans-serif;
    position: relative;
  }
  .card {
    position: absolute;
    width: 560px;
    height: 320px;
    border-radius: 22px;
    overflow: hidden;
    background: linear-gradient(160deg, var(--card-top), var(--card-bottom));
    border: 2px solid var(--gold-deep);
  }
  .card--front { left: 27px; top: 230px; }
  .card--back { left: 613px; top: 230px; }

  .wordmark { display: flex; align-items: center; gap: 12px; color: var(--blue); font-weight: 800; }
  .wordmark__dot { border-radius: 50%; background: var(--gold); flex: none; }
  .wordmark__name { line-height: 1.05; text-transform: uppercase; letter-spacing: 0.5px; }
  .wordmark__name span { display: block; }

  .card--front .wordmark { position: absolute; left: 0; right: 0; top: 92px; justify-content: center; }
  .card--front .wordmark__dot { width: 58px; height: 58px; }
  .card--front .wordmark__name span:first-child { font-size: 44px; }
  .card--front .wordmark__name span:last-child { font-size: 19px; }
  .services {
    position: absolute; left: 0; right: 0; top: 210px;
    text-align: center; color: var(--gold); font-weight: 400; font-size: 21px; letter-spacing: 0.5px;
  }

  .card--back .wordmark { position: absolute; right: 30px; top: 26px; gap: 8px; }
  .card--back .wordmark__dot { width: 32px; height: 32px; }
  .card--back .wordmark__name span:first-child { font-size: 26px; }
  .card--back .wordmark__name span:last-child { font-size: 11px; }

  .rule { position: absolute; height: 1.5px; background: var(--gold); }
  .rule--main { left: 32px; right: 30px; top: 128px; }

  .person { position: absolute; left: 32px; top: 80px; color: var(--gold); }
  .person__name { font-weight: 800; font-size: 22px; letter-spacing: 0.5px; text-transform: uppercase; }
  .person__role { font-weight: 400; font-size: 14px; margin-top: 2px; }

  .company { position: absolute; left: 32px; top: 142px; color: var(--ink-soft); font-size: 13px; line-height: 1.35; }
  .contacts { position: absolute; left: 32px; top: 186px; list-style: none; color: var(--gold); font-size: 13px; }
  .contacts li { display: flex; align-items: center; gap: 8px; height: 21px; }
  .contacts svg { width: 13px; height: 13px; fill: var(--gold); flex: none; }

  .credentials {
    position: absolute; right: 30px; top: 160px; text-align: right;
    color: var(--gold); font-size: 13px; line-height: 1.5;
  }
  .band { position: absolute; left: 0; bottom: 0; width: 560px; height: 80px; }
</style>
</head>
<body>

<section class="card card--front" aria-label="Business card front">
  <div class="wordmark">
    <span class="wordmark__dot"></span>
    <div class="wordmark__name"><span>Z-9 Max</span><span>Emergency Restoration</span></div>
  </div>
  <p class="services">• Water • Mold • Fire • Restoration</p>
</section>

<section class="card card--back" aria-label="Business card back">
  <div class="wordmark">
    <span class="wordmark__dot"></span>
    <div class="wordmark__name"><span>Z-9 Max</span><span>Emergency Restoration</span></div>
  </div>

  <div class="person">
    <h1 class="person__name">Derek Vannorman</h1>
    <p class="person__role">Owner</p>
  </div>
  <div class="rule rule--main"></div>

  <p class="company">Z-9 Max<br>Emergency Restoration</p>

  <ul class="contacts">
    <li>
      <svg viewBox="0 0 24 24" aria-hidden="true"><path d="M6.6 10.8a15 15 0 0 0 6.6 6.6l2.2-2.2c.3-.3.7-.4 1-.2 1.1.4 2.3.6 3.6.6.6 0 1 .4 1 1V20c0 .6-.4 1-1 1C10.6 21 3 13.4 3 4c0-.6.4-1 1-1h3.5c.6 0 1 .4 1 1 0 1.3.2 2.5.6 3.6.1.3 0 .7-.2 1z"/></svg>
      (555)412-7083
    </li>
    <li>
      <svg viewBox="0 0 24 24" aria-hidden="true"><path d="M2 5h20v14H2zm2 2v.5l8 5 8-5V7zm0 3v7h16v-7l-8 5z"/></svg>
      z9maxbuild@mailbox.test
    </li>
    <li>
      <svg viewBox="0 0 24 24" aria-hidden="true"><path d="M12 2a10 10 0 1 0 0 20 10 10 0 0 0 0-20zm0 2c.9 0 2.2 1.8 2.7 5H9.3C9.8 5.8 11.1 4 12 4zm-3.9 7h7.8c0 .7 0 1.3-.1 2H8.2c-.1-.7-.1-1.3-.1-2zm.2 4h7.4c-.5 3.2-1.8 5-2.7 5s-2.200-1.8-2.7-5zM4.1 11h2c0 .7 0 1.3.1 2h-2a8 8 0 0 1-.1-2zm13.8 0h2a8 8 0 0 1-.1 2h-2c.1-.7.1-1.3.1-2z"/></svg>
      www.z9maxbuild.test
    </li>
  </ul>

  <div class="credentials">
    <p>Lic #4702859 D-47 K</p>
    <p>RVFTA Certified #81254039</p>
  </div>

  <svg class="band" viewBox="0 0 560 80" preserveAspectRatio="none" aria-hidden="true">
    <defs>
      <linearGradient id="goldBand" x1="0" y1="0" x2="1" y2="0">
        <stop offset="0" stop-color="#a8742a"/>
        <stop offset="0.55" stop-color="#eccb7c"/>
        <stop offset="1" stop-color="#c28a38"/>
      </linearGradient>
      <linearGradient id="blueBand" x1="0" y1="0" x2="1" y2="0">
        <stop offset="0" stop-color="#2f5fb8"/>
        <stop offset="1" stop-color="#6ea8e6"/>
      </linearGradient>
    </defs>
    <polygon points="0,54 380,54 398,36 390,36 372,48 0,48" fill="url(#blueBand)"/>
    <polygon points="0,60 392,60 420,30 560,30 560,80 0,80" fill="url(#goldBand)"/>
  </svg>
</section>

</body>
</html>
```